Ordnerdesign für Experte für Versicherungs - und Haftungsfragen im Etiketten - und Verpackungsdruck
Ordnerdesign für Experte für Versicherungs - und Haftungsfragen im Etiketten - und Verpackungsdr..
Zielgruppe
Ich bin Henrik Wallmoser Experte für Versicherungs - und Haftungsfragen im Etiketten - und Verpackungsdruck (meine CI Farben sind orange /schwarz ) Meine Company und das Produkt ist die tarvolink und der tarvolnk Schutzbrief für Druckerereien (schwarz/gelb)
Aufgabenstellung
Gesucht wird für mein/unser Projekt : Ordnerdesign PLUS Register eines Notfallhandbuchs für Unternehmer . Es gibt zwei Produktlinien - zu beiden ist jeweils der Farbfächer /Broschüre beigefügt : Entweder der Notfallordner soll unter ' Henrik Wallmoser Experte für Haftungsfragen .. ( Orange Schwarz oder die Farben meiner Company ( tarvolink Schwarz - gelb ) siehe Broschüre angelegt werden. freie Hand , was also besser passt .

```html
<!DOCTYPE html>
<html lang="de">
<head>
<meta charset="utf-8">
<title>Notfallplan – Ordnerdesign</title>
<link href="https://fonts.googleapis.com/css2?family=Archivo:wght@500;700&display=swap" rel="stylesheet">
<style>
  :root {
    --stage: #ececec;
    --cover: #25262e;
    --accent: #ff4a2b;
    --accent-deep: #e8391d;
    --label: #f7f7f7;
    --metal: #c9bfa6;
    --metal-dark: #6f6654;
  }
  html, body {
    margin: 0;
    width: 1200px;
    height: 801px;
    overflow: hidden;
    background: var(--stage);
    font-family: "Archivo", Arial, sans-serif;
  }
  .binder {
    position: absolute;
    left: 290px;
    top: 70px;
    width: 620px;
    height: 660px;
    display: flex;
    box-shadow: 0 18px 40px rgba(0,0,0,0.18);
  }
  .binder__spine {
    position: relative;
    width: 110px;
    background: var(--accent);
    border-right: 3px solid var(--accent-deep);
  }
  .spine-label {
    position: absolute;
    left: 18px;
    top: 30px;
    width: 74px;
    height: 300px;
    background: var(--label);
    border: 1px solid #d9d9d9;
  }
  .spine-finger-hole {
    position: absolute;
    left: 33px;
    top: 430px;
    width: 40px;
    height: 40px;
    border-radius: 50%;
    background: var(--metal-dark);
    border: 3px solid var(--metal);
  }
  .binder__cover {
    position: relative;
    flex: 1;
    background: var(--cover);
  }
  .cover-rivet {
    position: absolute;
    left: 26px;
    width: 26px;
    height: 60px;
  }
  .cover-rivet--top { top: 170px; }
  .cover-rivet--bottom { top: 400px; }
  .cover-title {
    position: absolute;
    left: 150px;
    top: 250px;
    margin: 0;
    color: var(--accent);
    font-weight: 700;
    font-size: 30px;
    letter-spacing: 0.5px;
    line-height: 1;
  }
  .cover-subtitle {
    position: absolute;
    left: 150px;
    top: 292px;
    margin: 0;
    color: var(--accent);
    font-weight: 500;
    font-size: 15px;
    line-height: 1.3;
  }
  .cover-signature {
    position: absolute;
    left: 250px;
    top: 470px;
    width: 200px;
    height: 80px;
    background: linear-gradient(90deg, rgba(255,74,43,0.35), rgba(255,74,43,0.15));
  }
</style>
</head>
<body>
  <div class="binder">
    <div class="binder__spine">
      <div class="spine-label"></div>
      <div class="spine-finger-hole"></div>
    </div>
    <div class="binder__cover">
      <svg class="cover-rivet cover-rivet--top" viewBox="0 0 26 60">
        <rect x="2" y="2" width="22" height="56" rx="11" fill="none" stroke="#c9bfa6" stroke-width="3"/>
        <rect x="8" y="10" width="10" height="40" rx="5" fill="#6f6654"/>
      </svg>
      <svg class="cover-rivet cover-rivet--bottom" viewBox="0 0 26 60">
        <rect x="2" y="2" width="22" height="56" rx="11" fill="none" stroke="#c9bfa6" stroke-width="3"/>
        <rect x="8" y="10" width="10" height="40" rx="5" fill="#6f6654"/>
      </svg>
      <h1 class="cover-title">NOTFALLPLAN</h1>
      <p class="cover-subtitle">für Unternehmer im Etiketten -<br>und Verpackungsdruck.</p>
      <div class="cover-signature" role="img" aria-label="Handschriftliche Unterschrift in Orange"></div>
    </div>
  </div>
</body>
</html>
```